Halloween graphics for black and white brimzo game

We currently have a black and white brimzo game, and we want to launch a Halloween-themed version. I need a designer to take a whole bunch of graphics and put a Halloween theme on them.

Note the exact size and depth of the files must be preserved. Most of the graphics are black and white (2-bit), while a few are 16 color grayscale. Also, the files must all be gifs.

Note though there are a lot of graphics, most of it should be pretty quick. Most are small, and most are black and white (2-bit.) You could integrate things like skulls, bats, ghosts, and pumpkins to the graphics to make them halloween-like.

• All files must be in GIF format
All files must be the same exact dimensions and depth as the original files
Must put a Halloween theme on the graphics

```html
<!DOCTYPE html>
<html lang="en">
<head>
<meta charset="utf-8">
<title>Stack Drop – Nightfall Edition</title>
<link href="https://fonts.googleapis.com/css2?family=Archivo+Black&family=Fira+Sans+Condensed:wght@700;800&display=swap" rel="stylesheet">
<style>
  :root {
    --paper: #ffffff;
    --ink: #111111;
    --dark: #333333;
    --title: #555555;
    --mid: #8a8a8a;
    --light: #cfcfcf;
    --soft: #e4e4e4;
    --shadow: rgba(0,0,0,0.35);
  }
  * { box-sizing: border-box; margin: 0; padding: 0; }
  html, body { width: 1200px; height: 720px; overflow: hidden; background: var(--paper); }
  .canvas { position: relative; width: 1200px; height: 720px; background: var(--paper); font-family: "Fira Sans Condensed", sans-serif; color: var(--ink); }

  .loading { position: absolute; left: 429px; top: 82px; font-family: "Archivo Black", sans-serif; font-size: 44px; line-height: 1; color: var(--mid); -webkit-text-stroke: 2px var(--ink); letter-spacing: 1px; }
  .loading-bat { position: absolute; left: 668px; top: 58px; width: 54px; height: 54px; background: linear-gradient(160deg, #444, #111); border-radius: 6px; }

  .side-bar { position: absolute; left: 129px; top: 200px; width: 7px; height: 480px; background: var(--mid); }
  .side-badge { position: absolute; left: 136px; top: 200px; width: 117px; height: 127px; background: var(--soft); padding: 12px 0 0 9px; }
  .side-badge-name { font-weight: 800; font-size: 22px; line-height: 1; color: var(--dark); }
  .side-badge-mark { position: absolute; right: 14px; bottom: 10px; width: 48px; height: 48px; background: var(--mid); }
  .next-label { position: absolute; left: 181px; top: 330px; font-weight: 700; font-size: 12px; }

  .controls { position: absolute; left: 140px; top: 580px; width: 116px; height: 92px; font-weight: 700; font-size: 12px; }
  .controls span { position: absolute; }
  .ctl-rotate { left: 33px; top: 0; }
  .ctl-left { left: 2px; top: 40px; }
  .ctl-right { right: 0; top: 40px; }
  .ctl-drop { left: 38px; bottom: 0; }
  .dpad { position: absolute; left: 32px; top: 17px; width: 58px; height: 58px; }

  .playfield { position: absolute; left: 296px; top: 203px; width: 379px; height: 480px; border: 4px solid var(--ink); border-radius: 6px; background: var(--paper); }
  .corner { position: absolute; width: 18px; height: 14px; background: var(--light); border-radius: 3px; }
  .corner.tl { left: 18px; top: 18px; } .corner.tr { right: 18px; top: 18px; }
  .corner.bl { left: 18px; bottom: 18px; } .corner.br { right: 18px; bottom: 18px; }

  .game-name { position: absolute; left: 751px; top: 222px; font-weight: 800; font-size: 78px; line-height: 0.95; letter-spacing: 2px; color: var(--title); }

  .piece { position: absolute; }
  .tile { position: absolute; border: 2px solid var(--ink); box-shadow: 4px 5px 4px var(--shadow); }
  .tile::after { content: ""; position: absolute; inset: 5px; border: 1px solid var(--mid); }
  .tile.ghost { background: radial-gradient(circle, #f2f2f2 28%, #1a1a1a 32%); }
  .tile.bat { background: radial-gradient(ellipse 40% 25%, #1a1a1a 60%, #dcdcdc 66%); }
  .tile.spider { background: radial-gradient(circle, #1a1a1a 26%, #e0e0e0 32%); }

  .edition { position: absolute; left: 704px; top: 616px; width: 379px; height: 47px; background: var(--ink); color: var(--paper); font-weight: 700; font-size: 34px; line-height: 47px; text-align: center; }
</style>
</head>
<body>
<div class="canvas">
  <div class="loading">Loading...</div>
  <div class="loading-bat" role="img" aria-label="Flying bat illustration"></div>

  <div class="side-bar"></div>
  <div class="side-badge">
    <div class="side-badge-name">STACK<br>DROP</div>
    <div class="side-badge-mark"></div>
  </div>
  <div class="next-label">Next</div>

  <div class="controls">
    <span class="ctl-rotate">Rotate</span>
    <span class="ctl-left">Left</span>
    <span class="ctl-right">Right</span>
    <span class="ctl-drop">Drop</span>
    <svg class="dpad" viewBox="0 0 58 58" aria-hidden="true">
      <rect x="4" y="4" width="50" height="50" rx="8" fill="#555" stroke="#111" stroke-width="2"/>
      <circle cx="29" cy="29" r="10" fill="#777" stroke="#222" stroke-width="2"/>
      <path d="M29 6 l6 8 h-12z M29 52 l6 -8 h-12z M6 29 l8 6 v-12z M52 29 l-8 6 v-12z" fill="#ddd"/>
    </svg>
  </div>

  <div class="playfield">
    <span class="corner tl"></span><span class="corner tr"></span>
    <span class="corner bl"></span><span class="corner br"></span>
  </div>

  <div class="game-name">STACK<br>DROP</div>

  <div class="piece" role="img" aria-label="Block piece with ghost tiles">
    <div class="tile ghost" style="left:763px;top:417px;width:40px;height:40px"></div>
    <div class="tile ghost" style="left:723px;top:457px;width:40px;height:40px"></div>
    <div class="tile ghost" style="left:763px;top:457px;width:40px;height:40px"></div>
    <div class="tile ghost" style="left:723px;top:497px;width:40px;height:40px"></div>
  </div>
  <div class="piece" role="img" aria-label="Square block piece with bat tiles">
    <div class="tile bat" style="left:848px;top:488px;width:42px;height:42px"></div>
    <div class="tile bat" style="left:890px;top:488px;width:42px;height:42px"></div>
    <div class="tile bat" style="left:848px;top:530px;width:42px;height:42px"></div>
    <div class="tile bat" style="left:890px;top:530px;width:42px;height:42px"></div>
  </div>
  <div class="piece" role="img" aria-label="Block piece with spider tiles">
    <div class="tile spider" style="left:971px;top:416px;width:40px;height:40px"></div>
    <div class="tile spider" style="left:1011px;top:416px;width:40px;height:40px"></div>
    <div class="tile spider" style="left:971px;top:456px;width:40px;height:40px"></div>
    <div class="tile spider" style="left:971px;top:496px;width:40px;height:40px"></div>
  </div>

  <div class="edition">Nightfall Edition</div>
</div>
</body>
</html>
```